Improving a camping website homepage header*

My client is very happy with his new website and its new functionalities. However, he's not very happy about the homepage design. Specifically, the header(this includes the menu, large header image and two columns beneath that). You can find the website here: http://linkhop.example/tentsiteDemo .

He forwarded me several other websites he likes. Which can be found in the attachments. I also included several pictures of the camping.

I'm looking for a design that will improve the header of the homepage with room for other global style chances. The logo cannot be changed.

Attachments
1) His old website homepage
2) Website mockup he liked.
3) Another website mockup he liked.

Other images can be found on the new website http://linkhop.example/tentsiteDemo or his old website http://linkhop.example/priorTentsiteDemo.

Can you help us?
Updates

Hello guys. Here's a bit more information - Language used on the website is dutch. - The two columns left/right are supposed to link to Hire/Buy chalets. The client indicated that he finds these links important, but doesn't like the current design. I think this is partially the case because he doesn't like the icons. I'm looking forward to your designs!

Target Market(s)

30-50 year old wealthy people that want to purchase or rent cabins in the Netherlands.

Number of Pages Required

1 page

Colors

Designer to choose colors to be used in the design.

Requirements
Must have
• Improved header
Nice to have
• Global style changes
Should not have
• Logo changes

```html
<!DOCTYPE html>
<html lang="nl">
<head>
<meta charset="utf-8">
<title>Parc Lindehof</title>
<link href="https://fonts.googleapis.com/css2?family=Ubuntu:wght@400;500&display=swap" rel="stylesheet">
<style>
:root{
  --green:#8db34a;
  --green-dark:#6f9a2e;
  --orange:#f7941d;
  --black:#000;
  --ink:#222;
  --muted:#9a9a9a;
  --white:#fff;
}
*{box-sizing:border-box;margin:0;padding:0}
html,body{width:816px;height:1200px;overflow:hidden}
body{position:relative;background:var(--white);font-family:'Ubuntu',sans-serif;color:var(--ink)}
.abs{position:absolute}
.topbar{left:0;top:0;width:816px;height:20px;background:var(--black)}
.brand{left:36px;top:36px;display:flex;align-items:center;gap:6px;color:var(--green-dark);font-size:13px;font-weight:500}
.brand-dot{width:14px;height:14px;border-radius:50%;background:var(--green)}
.nav{left:251px;top:20px;height:60px;display:flex;align-items:center;font-size:11.5px;font-weight:500;color:var(--ink)}
.nav a{color:inherit;text-decoration:none;margin-right:20px}
.nav .active{background:var(--green);color:var(--white);height:60px;width:54px;display:flex;align-items:center;justify-content:center;margin-right:9px}
.login{left:696px;top:39px;width:88px;height:23px;background:var(--orange);color:var(--white);font-size:11.5px;display:flex;align-items:center;border-radius:2px}
.login .search{width:20px;height:23px;background:#e6861a;display:flex;align-items:center;justify-content:center;margin-right:9px}
.hero{left:32px;top:81px;width:752px;height:320px;background:linear-gradient(160deg,#c9d6e0 0%,#8a8f7a 30%,#b8762e 60%,#6c4a22 85%,#3f4a2a 100%)}
.hero-panel{left:32px;top:336px}
.cta{color:var(--white);font-size:14px;display:flex;align-items:center;gap:10px}
.call{left:552px;top:432px;color:var(--white);display:flex;align-items:center;gap:6px;font-size:13px}
.call strong{font-size:20px;font-weight:400;margin-left:14px;letter-spacing:1px}
.section-title{left:59px;top:480px;font-size:29px;font-weight:500;line-height:36px;z-index:5;white-space:nowrap}
.section-title span{color:var(--orange)}
.card{width:192px;height:203px;background:var(--white);box-shadow:1px 1px 3px rgba(0,0,0,.18);z-index:1}
.card .photo{position:absolute;left:0;top:40px;width:192px;height:77px}
.card h3{position:absolute;left:0;top:124px;font-size:11px;font-weight:500}
.card .price{position:absolute;left:1px;top:142px;font-size:7px;color:var(--orange)}
.card .meta{position:absolute;left:2px;top:159px;font-size:5px;color:var(--muted)}
.card .more{position:absolute;right:8px;top:169px;background:var(--orange);color:var(--white);font-size:7px;padding:3px 8px}
.card .tools{position:absolute;right:8px;top:190px;font-size:6px;color:#bbb;letter-spacing:11px}
.ph-a{background:linear-gradient(180deg,#c8d0c8,#9fa59b 55%,#4d6a38)}
.ph-b{background:linear-gradient(180deg,#9ab27c,#cfd3c8 50%,#4f7d2c)}
.ph-c{background:linear-gradient(180deg,#5a3e2c,#b6642a 50%,#8a7a62)}
.footer{left:32px;top:913px;width:752px;height:238px;background:var(--green);color:var(--white)}
.footer h4{position:absolute;font-size:16px;font-weight:400}
.thumb{position:absolute;width:144px;height:73px;background:var(--white)}
.thumb .photo{height:60px}
.thumb p{display:flex;justify-content:space-between;font-size:5.5px;padding:3px 4px;color:var(--ink)}
.thumb p span{color:var(--orange)}
.social{position:absolute;left:433px;width:26px;height:26px;border-radius:50%;background:var(--black)}
.contact-row{position:absolute;left:568px;display:flex;gap:8px;font-size:10px;line-height:1.4}
.contact-row svg{flex:none}
.bottombar{left:0;top:1151px;width:816px;height:49px;background:var(--black);color:var(--white);font-size:9px;display:flex;align-items:center;justify-content:center}
</style>
</head>
<body>
<div class="abs topbar"></div>

<div class="abs brand"><span class="brand-dot"></span>Parc Lindehof</div>

<nav class="abs nav">
  <a class="active" href="#">Home</a>
  <a href="#">Het Park</a>
  <a href="#">Financiering</a>
  <a href="#">Aanbiedingen</a>
  <a href="#">Faciliteiten</a>
  <a href="#">Contact</a>
</nav>
<div class="abs login"><span class="search"><svg width="10" height="10" viewBox="0 0 10 10"><circle cx="6" cy="4" r="3" fill="none" stroke="#000" stroke-width="1.2"/><line x1="4" y1="6" x2="1" y2="9" stroke="#000" stroke-width="1.2"/></svg></span>Inloggen</div>

<div class="abs hero" role="img" aria-label="Houten chalet op een zonnige berghelling met lariksen en rotspieken"></div>

<svg class="abs hero-panel" width="752" height="145" viewBox="0 0 752 145">
  <polygon points="0,0 320,0 384,65 752,65 752,145 0,145" fill="var(--green)"/>
</svg>

<div class="abs cta" style="left:149px;top:360px">Chalet Kopen
  <svg width="30" height="30" viewBox="0 0 30 30"><path d="M4 20 Q10 14 18 17 L24 16 L24 20 L14 24 Z" fill="#111"/><rect x="14" y="6" width="12" height="7" rx="1" fill="#111"/><circle cx="20" cy="9.5" r="2" fill="var(--green)"/></svg>
</div>
<div class="abs cta" style="left:149px;top:416px">Chalet Huren
  <svg width="30" height="34" viewBox="0 0 30 34"><path d="M4 4 L26 4 L24 9 L18 10 L17 24 L13 24 L12 10 L6 9 Z" fill="#111"/><circle cx="15" cy="28" r="3" fill="none" stroke="#111" stroke-width="2"/></svg>
</div>

<div class="abs call">
  <svg width="22" height="22" viewBox="0 0 22 22"><path d="M4 2 L8 6 L6 9 Q9 14 13 16 L16 14 L20 18 L17 21 Q6 19 1 5 Z" fill="#222"/></svg>
  Call Us <strong>030 - 12 34 56</strong>
</div>

<article class="abs card" style="left:60px;top:484px"><div class="photo ph-a" role="img" aria-label="Lichtgrijs chalet met tuinset"></div><h3>Kavel 190</h3><p class="price">$350 Per Maand</p><p class="meta">▭ 3 &nbsp; ▭ 2 &nbsp; ▭ 100,00 m²</p><span class="more">Lees meer</span><span class="tools">‹♥+</span></article>
<article class="abs card" style="left:312px;top:484px"><div class="photo ph-b" role="img" aria-label="Stacaravan in een groene tuin"></div><h3>Kavel 233</h3><p class="price">$ 205.000</p><p class="meta">▭ 1 &nbsp; ▭ 1 &nbsp; ▭ 130,00 m²</p><span class="more">Lees meer</span><span class="tools">‹♥+</span></article>
<article class="abs card" style="left:569px;top:484px"><div class="photo ph-c" role="img" aria-label="Houten blokhut chalet"></div><h3>Kavel 236</h3><p class="price">$ 195.000</p><p class="meta">▭ 3 &nbsp; ▭ 2 &nbsp; ▭ 100,00 m²</p><span class="more">Lees meer</span><span class="tools">‹♥+</span></article>

<article class="abs card" style="left:60px;top:697px"><div class="photo ph-c" role="img" aria-label="Houten blokhut chalet"></div><h3>Kavel 190</h3><p class="price">$350 Per Maand</p><p class="meta">▭ 3 &nbsp; ▭ 2 &nbsp; ▭ 100,00 m²</p><span class="more">Lees meer</span><span class="tools">‹♥+</span></article>
<article class="abs card" style="left:311px;top:697px"><div class="photo ph-a" role="img" aria-label="Lichtgrijs chalet met tuinset"></div><h3>Kavel 233</h3><p class="price">$ 205.000</p><p class="meta">▭ 1 &nbsp; ▭ 1 &nbsp; ▭ 130,00 m²</p><span class="more">Lees meer</span><span class="tools">‹♥+</span></article>
<article class="abs card" style="left:569px;top:697px"><div class="photo ph-b" role="img" aria-label="Stacaravan in een groene tuin"></div><h3>Kavel 236</h3><p class="price">$ 195.000</p><p class="meta">▭ 3 &nbsp; ▭ 2 &nbsp; ▭ 100,00 m²</p><span class="more">Lees meer</span><span class="tools">‹♥+</span></article>

<h2 class="abs section-title"><span>R</span>ecente Chalets</h2>

<footer class="abs footer">
  <h4 style="left:63px;top:18px">New Chalets</h4>
  <div class="thumb" style="left:48px;top:52px"><div class="photo ph-a" role="img" aria-label="Lichtgrijs chalet"></div><p>Kavel 190<span>$390 Per Maand</span></p></div>
  <div class="thumb" style="left:216px;top:52px"><div class="photo ph-c" role="img" aria-label="Houten chalet"></div><p>Kavel 190<span>$390 Per Maand</span></p></div>
  <div class="thumb" style="left:48px;top:149px"><div class="photo ph-b" role="img" aria-label="Stacaravan"></div><p>Kavel 190<span>$390 Per Maand</span></p></div>
  <div class="thumb" style="left:218px;top:149px"><div class="photo ph-a" role="img" aria-label="Lichtgrijs chalet"></div><p>Kavel 190<span>$390 Per Maand</span></p></div>

  <h4 style="left:401px;top:18px">Social media</h4>
  <span class="social" style="top:55px" aria-label="Social media link"></span>
  <span class="social" style="top:89px" aria-label="Social media link"></span>
  <span class="social" style="top:123px" aria-label="Social media link"></span>
  <span class="social" style="top:157px" aria-label="Social media link"></span>
  <span class="social" style="top:191px" aria-label="Social media link"></span>

  <h4 style="left:583px;top:18px">Contact</h4>
  <div class="contact-row" style="top:50px"><svg width="18" height="14" viewBox="0 0 18 14"><rect x="1" y="1" width="16" height="12" fill="#111"/><path d="M1 1 L9 8 L17 1" stroke="var(--green)" fill="none"/></svg><span>Beukenlaan 14<br>4210 AB Heuvelrijk</span></div>
  <div class="contact-row" style="top:90px"><svg width="18" height="14" viewBox="0 0 18 14"><path d="M2 5 Q9 -1 16 5 L14 7 L12 5 L6 5 L4 7 Z" fill="#111"/><rect x="4" y="7" width="10" height="7" fill="#111"/></svg><span>0300 - 12 34 56</span></div>
  <div class="contact-row" style="top:119px"><svg width="18" height="16" viewBox="0 0 18 16"><rect x="2" y="5" width="14" height="10" fill="#111"/><rect x="5" y="1" width="8" height="5" fill="#111"/></svg><span>0300 - 65 43 21</span></div>
  <div class="contact-row" style="top:147px"><svg width="18" height="14" viewBox="0 0 18 14"><rect x="1" y="2" width="16" height="10" fill="none" stroke="#111" stroke-width="1.5"/><path d="M1 2 L17 12 M17 2 L1 12" stroke="#111" stroke-width="1.2"/></svg><span>info@parclindehof.example</span></div>
  <div class="contact-row" style="top:176px"><svg width="18" height="16" viewBox="0 0 18 16"><circle cx="9" cy="8" r="7" fill="none" stroke="#111" stroke-width="1.5"/><path d="M6 6 Q9 3 12 6 M6 10 Q9 13 12 10" stroke="#111" fill="none"/></svg><span>parcLindehofChat</span></div>
  <div class="contact-row" style="top:208px"><svg width="18" height="16" viewBox="0 0 18 16"><rect x="3" y="1" width="12" height="9" fill="#111"/><rect x="1" y="11" width="16" height="3" fill="#111"/></svg><span>http://parc-lindehof.example</span></div>
</footer>

<div class="abs bottombar">Copyright 2018 | Parc Lindehof</div>
</body>
</html>
```